Explainer Video Landing Page

We will soon have an "explainer" video which will explain to people in a graphical way what it is we do and the solutions we provide. Our current landing page design, located at http://www.relaynetvista.com has a lot of different elements that we like, but won't focus on the new video we have as the "hero". We will want this new landing page to really showcase the video. Some of the other design elements we need are :
1- A link to "Get a Quote Online", in some way. This is the "goal" of the landing page.
2- We'll want some content sections under the video
3- We'll want the lead gen form to be there as well.
As an example, have a look at what BrightOwl did. http://www.brightowl.com/
We like their example, but find it a bit busy. Our design should be cleaner with more whitespace. They are doing a lot of good things on that page that we'll want to mimic, like adding testimonials and existing customer logos.
Thank you in advance for participating in our design project.
Target Market(s)
Small and Mid-size Businesses. This will be a B2B landing page, focused on the communications needs of business.
Look and feel

```html
<!DOCTYPE html>
<html lang="en">
<head>
<meta charset="utf-8">
<title>Corvance – Business VoIP Phone Service</title>
<link href="https://fonts.googleapis.com/css2?family=Jost:wght@400;500;600&display=swap" rel="stylesheet">
<style>
:root{
  --orange:#f07a22;
  --teal:#12a58b;
  --teal-dark:#0e8a74;
  --pink:#e8197b;
  --ink:#222;
  --body:#444;
  --grey-band:#efefef;
  --line:#e2e2e2;
  --black:#000;
}
*{box-sizing:border-box;margin:0;padding:0}
html,body{width:1200px;height:2413px;overflow:hidden;background:#fff}
body{font-family:Arial,Helvetica,sans-serif;color:var(--body);position:relative}
.abs{position:absolute}

/* header */
.site-header{position:absolute;left:0;top:0;width:1200px;height:153px;background:#fff}
.brand{position:absolute;left:0;width:1200px;top:52px;text-align:center}
.brand-mark{display:block;width:34px;height:34px;border-radius:50%;background:#222;margin:0 auto 8px}
.brand-name{font-family:'Jost',sans-serif;font-weight:600;font-size:22px;letter-spacing:8px;color:#111}
.main-nav{position:absolute;left:170px;top:132px;width:856px;height:45px;background:var(--teal);border-radius:3px;display:flex;z-index:2;box-shadow:0 2px 3px rgba(0,0,0,.12)}
.main-nav a{flex:1;color:#fff;text-decoration:none;font-size:14px;text-align:center;line-height:45px;border-right:1px solid rgba(255,255,255,.15)}
.main-nav a:last-child{border-right:0}
.main-nav a.is-active{background:var(--teal-dark);border-radius:3px 0 0 3px}

/* hero */
.hero{position:absolute;left:0;top:153px;width:1200px;height:595px;background:linear-gradient(#ececec,#f6f6f6 30%,#f4f4f4)}
.hero-title{position:absolute;left:0;width:1200px;top:52px;text-align:center;font-family:'Jost',sans-serif;font-weight:500;font-size:75px;line-height:76px;color:var(--orange);letter-spacing:-1px}
.hero-sub{position:absolute;left:0;width:1200px;top:118px;text-align:center;font-family:'Jost',sans-serif;font-weight:500;font-size:42px;line-height:50px;color:var(--teal)}
.hero-sub em{font-style:normal;color:var(--pink)}
.video-frame{position:absolute;left:169px;top:199px;width:533px;height:313px;background:#000;border-radius:8px;padding:7px}
.video-screen{width:100%;height:256px;background:linear-gradient(135deg,#4a4a4a,#262626 45%,#5a5a5a 75%,#303030);border-radius:3px 3px 0 0;position:relative}
.play-btn{position:absolute;left:50%;top:50%;width:66px;height:66px;margin:-33px 0 0 -33px;border-radius:50%;background:rgba(60,60,60,.75)}
.play-btn svg{position:absolute;left:22px;top:17px}
.video-controls{height:36px;background:linear-gradient(#2c2c2c,#1a1a1a);border-top:2px solid #3a3a3a;position:relative;color:#aaa;font-size:10px}
.video-controls .time{position:absolute;left:78px;top:12px}
.hero-copy{position:absolute;left:730px;top:196px;width:310px}
.hero-copy h2{font-family:'Jost',sans-serif;font-weight:500;font-size:23px;line-height:31px;color:var(--orange);text-transform:uppercase;white-space:nowrap}
.hero-copy p{margin-top:12px;font-size:13px;line-height:18.5px;color:#333;white-space:nowrap}
.btn-quote{position:absolute;left:732px;top:442px;width:291px;height:66px;border-radius:4px;background:linear-gradient(#f2338a,#d8156c);color:#fff;font-family:'Jost',sans-serif;font-weight:500;font-size:24px;line-height:66px;text-align:center;text-decoration:none;box-shadow:0 2px 3px rgba(0,0,0,.15)}
.hero-arrow{position:absolute;left:615px;top:510px}

/* welcome */
.welcome{position:absolute;left:0;top:748px;width:1200px;height:249px;background:var(--grey-band);border-bottom:1px solid #dcdcdc;text-align:center}
.welcome-mark{position:absolute;left:570px;top:-20px;width:60px;height:60px;border-radius:50%;background:#222}
.section-title{font-family:'Jost',sans-serif;font-weight:500;font-size:23px;text-transform:uppercase}
.welcome .section-title{position:absolute;left:0;width:1200px;top:72px;color:var(--orange)}
.welcome p{position:absolute;left:180px;width:840px;top:126px;font-size:13px;line-height:20.5px;color:#444}

/* clients */
.clients{position:absolute;left:0;top:997px;width:1200px;height:290px;text-align:center}
.clients .section-title{position:absolute;left:0;width:1200px;top:40px;color:var(--teal)}
.clients .lead{position:absolute;left:0;width:1200px;top:82px;font-size:22px;line-height:32px;color:var(--ink)}
.client-logo{position:absolute;top:174px;width:119px;height:61px;border:3px solid #e4e4e4;background:#fff;font-family:'Jost',sans-serif;font-weight:500;font-size:17px;line-height:55px;color:#2c5aa0;text-align:center}

/* demo */
.demo{position:absolute;left:0;top:1287px;width:1200px;height:338px;background:var(--orange);text-align:center;color:#fff}
.demo .section-title{position:absolute;left:0;width:1200px;top:42px;color:#fff}
.demo p{position:absolute;left:180px;width:840px;top:80px;font-size:13.5px;line-height:26px}
.demo p strong{font-weight:bold}
.field{position:absolute;width:267px;height:45px;background:#fff;border:1px solid #e0e0e0;color:#666;font-size:13.5px;line-height:45px;text-align:left;padding-left:11px}
.btn-demo{position:absolute;left:745px;top:228px;width:267px;height:45px;background:linear-gradient(#333,#1e1e1e);border-radius:3px;color:#fff;font-family:'Jost',sans-serif;font-weight:500;font-size:20px;line-height:45px}

/* testimonials */
.testimonials{position:absolute;left:0;top:1625px;width:1200px;height:519px}
.testimonials .section-title{position:absolute;left:0;width:1200px;top:40px;text-align:center;color:var(--teal)}
.quote-card{position:absolute;top:104px;width:245px;height:362px;background:#fff;border:1px solid #e6e6e6;box-shadow:0 1px 4px rgba(0,0,0,.12);overflow:hidden}
.quote-mark{position:absolute;top:-14px;font-family:Georgia,serif;font-weight:bold;font-size:170px;line-height:170px;color:#dcdcdc}
.quote-mark.open{left:14px}
.quote-mark.close{left:150px}
.avatar{position:absolute;left:74px;top:20px;width:96px;height:96px;border-radius:50%;border:3px solid #fff;box-shadow:0 0 0 1px #ddd}
.quote-card blockquote{position:absolute;left:17px;right:17px;top:146px;font-size:11.5px;line-height:20.8px;color:#222;font-style:italic}
.quote-card cite{display:block;font-style:normal;color:var(--orange);font-size:11.5px;line-height:20.8px}

/* footer */
.site-footer{position:absolute;left:0;top:2144px;width:1200px;height:269px;background:var(--black)}
.footer-col{position:absolute;top:30px}
.footer-col h4{font-family:'Jost',sans-serif;font-weight:500;font-size:13px;color:var(--teal);text-transform:uppercase;margin-bottom:8px}
.footer-col li{list-style:none;font-size:10.5px;line-height:20.6px;color:#fff}
.social li{padding-left:35px;position:relative}
.social li::before{content:"";position:absolute;left:0;top:3px;width:15px;height:15px;border-radius:50%;background:#777}
.footer-rule{position:absolute;left:190px;width:820px;top:193px;border-top:1px solid #262626}
.footer-legal{position:absolute;left:0;width:1200px;top:208px;text-align:center;font-size:10px;line-height:21px;color:#6a6a6a}
</style>
</head>
<body>

<header class="site-header">
  <div class="brand"><span class="brand-mark"></span><span class="brand-name">CORVANCE</span></div>
</header>
<nav class="main-nav">
  <a class="is-active" href="#">Home</a><a href="#">Plans &amp; Pricing</a><a href="#">Features</a><a href="#">Phones</a><a href="#">Resource</a><a href="#">Blog</a>
</nav>

<section class="hero">
  <h1 class="hero-title">FIND US IN YOUR CITY</h1>
  <div class="hero-sub">SERVING OVER <em>950</em> CANADIAN CITIES</div>

  <div class="video-frame">
    <div class="video-screen" role="img" aria-label="Explainer video still: a person on a phone beside a row of lights">
      <div class="play-btn"><svg width="30" height="32" viewBox="0 0 30 32"><path d="M0 0L30 16L0 32Z" fill="#d8d8d8"/></svg></div>
    </div>
    <div class="video-controls">
      <svg class="abs" style="left:12px;top:11px" width="50" height="12" viewBox="0 0 50 12"><path d="M0 0L9 6L0 12Z" fill="#888"/><path d="M30 4h4l5-4v12l-5-4h-4z" fill="#888"/></svg>
      <span class="time">00:00 / 10:46</span>
      <svg class="abs" style="left:355px;top:11px" width="150" height="12" viewBox="0 0 150 12"><rect x="0" y="1" width="12" height="9" fill="#888"/><rect x="22" y="1" width="12" height="9" fill="#888"/><circle cx="50" cy="6" r="5" fill="#888"/><circle cx="75" cy="6" r="4" fill="#888"/><rect x="92" y="1" width="14" height="10" fill="none" stroke="#999" stroke-width="2"/><rect x="116" y="1" width="14" height="10" fill="none" stroke="#999" stroke-width="2"/><rect x="138" y="1" width="12" height="10" fill="#888"/></svg>
    </div>
  </div>

  <div class="hero-copy">
    <h2>Corvance is the number<br>one choice for business<br>VoIP phone service in<br>Ottawa.</h2>
    <p>Lorem ipsum dolor sit amet, consectetur adipis<br>cing elit. Sed quis nisi euismod, fermentum<br>tellus a, lobortis quam. Vestibulum condimentum<br>mi vitae diam tristique, egestas dignissim diam<br>mattis</p>
  </div>
  <a class="btn-quote" href="#">GET A QUOTE ONLINE!</a>

  <svg class="hero-arrow" width="160" height="80" viewBox="0 0 160 80">
    <path d="M10 2C25 50 80 75 150 38" fill="none" stroke="var(--teal)" stroke-width="2"/>
    <path d="M138 34L152 37L144 48" fill="none" stroke="var(--teal)" stroke-width="2"/>
  </svg>
</section>

<section class="welcome">
  <span class="welcome-mark"></span>
  <h2 class="section-title">Welcome to Corvance</h2>
  <p>Cras accumsan orci mauris, ut aliquam ipsum faucibus sed. Fusce quam dui, accumsan a magna in, faucibus tristique lectus. Vestibulum sapien leo, placerat quis luctus eget, auctor et justo. Vestibulum ante ipsum primis in faucibus orci luctus et ultrices posuere cubilia Curae; Duis sagittis, risus ut viverra dignissim, lectus nunc iaculis arcu, et gravida est tortor ut erat. Morbi a feugiat dolor, in tristique elit.</p>
</section>

<section class="clients">
  <h2 class="section-title">Our Clients</h2>
  <p class="lead">Maecenas orci est, euismod facilisis feugiat sit amet, semper ut tortor.<br>Donec eleifend accumsan nisl, nec laoreet leo iaculis sit amet.</p>
  <div class="client-logo" style="left:193px">Harlow's</div>
  <div class="client-logo" style="left:331px">Visit Brenton</div>
  <div class="client-logo" style="left:468px">Starvale</div>
  <div class="client-logo" style="left:606px">Blendora</div>
  <div class="client-logo" style="left:745px">Morrow's</div>
  <div class="client-logo" style="left:883px">Lumicare</div>
</section>

<section class="demo">
  <h2 class="section-title">Sign up for a personalized demo.</h2>
  <p>A member of Corvance's marketing team will contact you to discuss your specific situation and see if Corvance's Hosted PBX is a good fit for your organization. Alternatively, give us a call at <strong>613-555-0187</strong> to speak to someone immediately.</p>
  <div class="field" style="left:188px;top:169px">First Name</div>
  <div class="field" style="left:466px;top:169px">Last Name</div>
  <div class="field" style="left:745px;top:169px">Company</div>
  <div class="field" style="left:188px;top:228px">Phone</div>
  <div class="field" style="left:466px;top:228px">Email</div>
  <div class="btn-demo">REQUEST A DEMO</div>
</section>

<section class="testimonials">
  <h2 class="section-title">“Testimonials”</h2>
  <article class="quote-card" style="left:190px">
    <span class="quote-mark open">“</span><span class="quote-mark close">”</span>
    <div class="avatar" role="img" aria-label="Portrait of Owen Hartley" style="background:linear-gradient(#c9383a,#d9a98a)"></div>
    <blockquote>Cras accumsan orci mauris, ut aliquam ipsum faucibus sed. Fusce quam dui, accumsan a magna in, faucibus tristique lectus. Vestibulum sapien leo, placerat quis luctus eget, auctor et justo. Vestibulum ante ipsum primis in faucibus orci luctus et ultrices posuere cubilia Curae<cite>Owen Hartley</cite><cite>Perth</cite></blockquote>
  </article>
  <article class="quote-card" style="left:479px">
    <span class="quote-mark open">“</span><span class="quote-mark close">”</span>
    <div class="avatar" role="img" aria-label="Portrait of Dale Brennick" style="background:linear-gradient(#3a3a3a,#c79a80 60%,#2a2a2a)"></div>
    <blockquote>Sed quis nisi euismod, fermentum tellus a, lobortis quam. Vestibulum condimentum mi vitae diam tristique, egestas dignissim diam mattis. Curabitur vel diam in massa porttitor dictum id in lorem. Vivamus faucibus ac leo ac dignissim. Maecenas orci est, euismod facilisis<cite>Dale Brennick</cite><cite>New York</cite></blockquote>
  </article>
  <article class="quote-card" style="left:767px">
    <span class="quote-mark open">“</span><span class="quote-mark close">”</span>
    <div class="avatar" role="img" aria-label="Portrait of Nora Castell" style="background:linear-gradient(#5a3a2a,#d9ad94 55%,#4a2e22)"></div>
    <blockquote>Vivamus eu magna rhoncus, consectetur metus ac, varius lacus. Donec ultricies, tortor quis sagittis sagittis, mauris erat ullamcorper augue, eu placerat diam nunc a lorem. Nam vulputate mauris id arcu pharetra, sed posuere quam cursus. Rauris erat ullamcorper augue<cite>Nora Castell</cite><cite>London</cite></blockquote>
  </article>
</section>

<footer class="site-footer">
  <div class="footer-col" style="left:190px">
    <h4>Features &amp; Benefits</h4>
    <ul><li>Included Features</li><li>Optional Features</li><li>Conferencing</li><li>Can I keep my Phone Number?</li><li>Corvance VoIP Phones</li><li>Money Back Guarantee</li></ul>
  </div>
  <div class="footer-col" style="left:431px">
    <h4>Resources</h4>
    <ul><li>What is Hosted PBX</li><li>Frequently Asked Questions</li><li>Testimonials</li><li>611 Online</li><li>Dashboard</li></ul>
  </div>
  <div class="footer-col" style="left:640px">
    <h4>Corvance</h4>
    <ul><li>Contact Us</li><li>Media Resources</li><li>Our History</li><li>Jobs</li><li>Corvance Vibe</li><li>Corvance Chats, our Blog</li></ul>
  </div>
  <div class="footer-col social" style="left:853px">
    <h4>Social</h4>
    <ul><li>Friendloop</li><li>Birdcall</li><li>Searchly</li><li>Clipstream</li><li>Workweb</li></ul>
  </div>
  <div class="footer-rule"></div>
  <div class="footer-legal">Call 1 877.555.0142 or email sales@corvance.com.<br>Copyright © 2014 Corvance. All rights reserved. This site has a Privacy policy.</div>
</footer>

</body>
</html>
```